American pesto sauce company needs a vintage/ old fashioned package design

Company name: Marisol Grove.
We need a food label design for 4 different flavors of pesto sauce: classic almond, sundried tomato, roasted red pepper, and Cajun spice. For those that do not know what pesto is, it is a sauce like tomato sauce that is traditionally Italian and goes on pasta or whatever you choose to put it on and the consistent ingredients are garlic, cheese, nuts, olive oil and basil. They are fresh, all natural without preservatives, artificial flavors or colors.
The design of the jar is an old fashioned wire bale jar used for preserving foods ( attached is a picture). I'm looking for a label with:
• an upscale vintage feel but will also stand out on a grocery store shelf. I have attached an example of the feel I am looking for as well as the format of the words with my company name.
• The word "Pesto" must be prominent on the label.
• metalic gold boarders that go around the whole label maybe with gold embellishments if you see fit for that upscale feeling.
• Also, as you can see in the attachment, there are different typesets. And it must be easy to read from at least 3 feet away.
• Each label will have a different color corresponding to the flavor- could be part of the flavor text
• The bottom of the front panel must have “Net Wt. 5.75 oz (162g)” in a creative format how you see fit. Measures: height-28 mm, width-75mm
• Need logo for top part of label with the letters MG for Marisol Grove and it will also contain the website, address and parent company name, use by date, etc. Measures:50 mm diameter
• The back panel of the label will contain the nutrition facts, ingredients and bar code. Measures: height-28 mm, width-75mm

Also the label is one piece with 3 different sections. Attached will be an example with measurements.
Updates

Check out this website on packaging. I absolutely love love love the Hartwell Pantry almond water labels. The colors for the different flavors. How its not just horizontal or vertical. The different typesets/fonts/typography. The flourishes and background thats faded.
http://brightwrapgallery.com/page/3/

Target Market(s)

Target market is medium- high income foodies between 35-65

Industry/Entity Type

Grocery Store

Requirements
Must have
• Net Wt on front lower panel. Separation of the company name Marisol & Pesto. See attachment.
Nice to have
• Name of flavor designed in a wave pattern as shown in attachment. Hand drawn font OK.

```html
<!DOCTYPE html>
<html lang="en">
<head>
<meta charset="utf-8">
<title>Marisol Grove Cajun Pepper Pesto – jar labels</title>
<link rel="stylesheet" href="https://fonts.googleapis.com/css2?family=Arimo:wght@700&family=Libre+Baskerville&family=Playfair+Display:ital,wght@1,900&family=Ribeye&display=swap">
<style>
  :root {
    --backdrop: #000000;
    --gold: #c9a94a;
    --gold-light: #e9d590;
    --pesto-red: #a3171b;
    --ink: #1d1a14;
    --logo-dark: #1f1b1c;
    --logo-text: #f4ecd0;
  }
  html, body {
    margin: 0;
    width: 1200px;
    height: 1200px;
    overflow: hidden;
    background: var(--backdrop);
  }
  .canvas { position: relative; width: 1200px; height: 1200px; }
  .label { position: absolute; top: 80px; width: 400px; height: 1050px; }
  .label svg { display: block; width: 400px; height: 1050px; }
  .label--cream {
    left: 107px;
    --panel: #f9f2cc;
    --panel-inner: #fcf8e2;
    --strap: #f5ecbf;
    --strap-word: #e6d89c;
    --flourish: #efe3b0;
  }
  .label--basil {
    left: 607px;
    --panel: #a9d46e;
    --panel-inner: #b8dc84;
    --strap: #cfe8ab;
    --strap-word: #b6d98a;
    --flourish: #9cc862;
  }
  .panel-fill { fill: var(--panel); stroke: var(--gold); stroke-width: 5; }
  .panel-rule { fill: none; stroke: var(--gold-light); stroke-width: 1.5; }
  .strap-fill { fill: var(--strap); stroke: var(--gold); stroke-width: 4; }
  .flourish-area { fill: var(--flourish); opacity: .6; }
  .strap-word { font-family: "Playfair Display", serif; font-style: italic; font-weight: 900; font-size: 38px; fill: var(--strap-word); text-anchor: middle; }
  .brand-name { font-family: "Libre Baskerville", serif; font-size: 15px; letter-spacing: 1.5px; fill: var(--ink); text-anchor: middle; }
  .flavor-name { font-family: "Ribeye", serif; font-size: 23px; fill: var(--pesto-red); text-anchor: middle; }
  .product-word { font-family: "Playfair Display", serif; font-style: italic; font-weight: 900; fill: var(--pesto-red); text-anchor: middle; }
  .tagline { font-family: "Ribeye", serif; font-size: 17px; fill: var(--pesto-red); text-anchor: middle; }
  .company-info { font-family: "Arimo", sans-serif; font-weight: 700; font-size: 11.5px; fill: var(--ink); text-anchor: middle; }
  .net-weight { font-family: "Arimo", sans-serif; font-weight: 700; font-size: 13px; fill: var(--ink); }
  .nutrition { font-family: "Arimo", sans-serif; font-weight: 700; font-size: 8.6px; fill: var(--ink); text-anchor: middle; }
  .logo-disc { fill: var(--logo-dark); stroke: var(--gold); stroke-width: 2; }
  .logo-initials { font-family: "Libre Baskerville", serif; font-size: 15px; fill: var(--logo-text); text-anchor: middle; }
</style>
</head>
<body>
<main class="canvas">

  <section class="label label--cream" aria-label="Cajun Pepper Pesto label, cream version">
    <svg viewBox="0 0 400 1050" xmlns="http://www.w3.org/2000/svg">
      <!-- neck strap -->
      <rect class="strap-fill" x="133" y="140" width="134" height="750"/>
      <g class="strap-words">
        <text class="strap-word" transform="rotate(180 200 212)" x="200" y="225">Pesto</text>
        <text class="strap-word" transform="rotate(180 200 265)" x="200" y="278">Pesto</text>
        <text class="strap-word" transform="rotate(180 200 315)" x="200" y="328">Pesto</text>
        <text class="strap-word" x="200" y="735">Pesto</text>
        <text class="strap-word" x="200" y="785">Pesto</text>
        <text class="strap-word" x="200" y="835">Pesto</text>
      </g>

      <!-- back panel: nutrition -->
      <path class="panel-fill" d="M40,7 H360 Q362,22 388,24 V128 Q362,130 360,145 H40 Q38,130 13,128 V24 Q38,22 40,7 Z"/>
      <path class="panel-rule" d="M46,15 H354 Q357,28 380,31 V121 Q357,124 354,137 H46 Q43,124 21,121 V31 Q43,28 46,15 Z"/>
      <g class="nutrition-block" transform="rotate(180 200 76)">
        <text class="nutrition" x="200" y="30">Nutrition Facts Serv. Size 1/4 cup (47g) Calories 200, Fat Cal. 190,</text>
        <text class="nutrition" x="200" y="40">Total Fat 22g (34% DV), Sat Fat 3.5g (18% DV), Cholest. 5mg (2%</text>
        <text class="nutrition" x="200" y="50">DV), Sodium 200mg (8% DV), Total Carb. 3g (1% DV), Fiber 1g (4% DV),</text>
        <text class="nutrition" x="200" y="60">Sugars 1g, Protein 3g, Vitamin A (4% DV), Vitamin C (4% DV), Calcium</text>
        <text class="nutrition" x="200" y="70">(4% DV), Iron (4% DV).</text>
        <text class="nutrition" x="200" y="80">Percent Daily Values (DV) are based on a 2,000 calorie diet. Not a</text>
        <text class="nutrition" x="200" y="90">significant source of trans fat. Ingredients: Extra virgin olive oil, onion,</text>
        <text class="nutrition" x="200" y="100">basil, almonds, parmesan cheese (cow's milk, rennet, cheese</text>
        <text class="nutrition" x="200" y="110">cultures, salt), garlic, sea salt, paprika, cayenne pepper, and spices.</text>
        <text class="nutrition" x="200" y="122">Contains: nuts and cheese.</text>
      </g>

      <!-- top seal -->
      <g transform="translate(200 512)">
        <path class="panel-fill" d="M152.4,63.1 A68,68 0 0 1 63.1,152.4 A68,68 0 0 1 -63.1,152.4 A68,68 0 0 1 -152.4,63.1 A68,68 0 0 1 -152.4,-63.1 A68,68 0 0 1 -63.1,-152.4 A68,68 0 0 1 63.1,-152.4 A68,68 0 0 1 152.4,-63.1 A68,68 0 0 1 152.4,63.1 Z"/>
        <path class="panel-rule" transform="scale(.92)" d="M152.4,63.1 A68,68 0 0 1 63.1,152.4 A68,68 0 0 1 -63.1,152.4 A68,68 0 0 1 -152.4,63.1 A68,68 0 0 1 -152.4,-63.1 A68,68 0 0 1 -63.1,-152.4 A68,68 0 0 1 63.1,-152.4 A68,68 0 0 1 152.4,-63.1 A68,68 0 0 1 152.4,63.1 Z"/>
        <ellipse class="flourish-area" role="img" aria-label="faded leaf flourishes behind the product name" cx="0" cy="-10" rx="120" ry="60"/>
      </g>
      <text class="brand-name" x="200" y="412">MARISOL GROVE</text>
      <circle class="logo-disc" cx="200" cy="440" r="21"/>
      <text class="logo-initials" x="200" y="446">MG</text>
      <text class="flavor-name" x="200" y="494">Cajun Pepper</text>
      <text class="product-word" x="200" y="545" font-size="54">Pesto</text>
      <text class="company-info" x="200" y="582">Orla Fine Foods, LLC.</text>
      <text class="company-info" x="200" y="596">218 Fennel Ave. Brookdale, NY</text>
      <text class="company-info" x="200" y="610">10457 +866-555-0192</text>
      <text class="company-info" x="200" y="624">www.marisolgrove.com</text>
      <text class="company-info" x="200" y="638">Ready to eat. Keep refrigerated, OK</text>
      <text class="company-info" x="200" y="652">to freeze</text>

      <!-- front panel -->
      <path class="panel-fill" d="M43,880 H357 Q359,895 385,897 V1021 Q359,1023 357,1038 H43 Q41,1023 16,1021 V897 Q41,895 43,880 Z"/>
      <path class="panel-rule" d="M49,888 H351 Q354,901 377,904 V1014 Q354,1017 351,1030 H49 Q46,1017 24,1014 V904 Q46,901 49,888 Z"/>
      <text class="brand-name" x="200" y="912" font-size="13">MARISOL GROVE</text>
      <text class="flavor-name" x="200" y="936" font-size="24">Cajun Pepper</text>
      <text class="product-word" x="200" y="992" font-size="62">Pesto</text>
      <text class="tagline" x="200" y="1018">most delicious</text>
      <text class="net-weight" x="30" y="927">Net Wt.</text>
      <text class="net-weight" x="30" y="950">5.75 oz</text>
      <text class="net-weight" x="30" y="973">(162g)</text>
      <circle class="logo-disc" cx="352" cy="955" r="21"/>
      <text class="logo-initials" x="352" y="961">MG</text>
    </svg>
  </section>

  <section class="label label--basil" aria-label="Cajun Pepper Pesto label, green version">
    <svg viewBox="0 0 400 1050" xmlns="http://www.w3.org/2000/svg">
      <rect class="strap-fill" x="133" y="140" width="134" height="750"/>
      <g class="strap-words">
        <text class="strap-word" transform="rotate(180 200 212)" x="200" y="225">Pesto</text>
        <text class="strap-word" transform="rotate(180 200 265)" x="200" y="278">Pesto</text>
        <text class="strap-word" transform="rotate(180 200 315)" x="200" y="328">Pesto</text>
        <text class="strap-word" x="200" y="735">Pesto</text>
        <text class="strap-word" x="200" y="785">Pesto</text>
        <text class="strap-word" x="200" y="835">Pesto</text>
      </g>

      <path class="panel-fill" d="M40,7 H360 Q362,22 388,24 V128 Q362,130 360,145 H40 Q38,130 13,128 V24 Q38,22 40,7 Z"/>
      <path class="panel-rule" d="M46,15 H354 Q357,28 380,31 V121 Q357,124 354,137 H46 Q43,124 21,121 V31 Q43,28 46,15 Z"/>
      <g class="nutrition-block" transform="rotate(180 200 76)">
        <text class="nutrition" x="200" y="30">Nutrition Facts Serv. Size 1/4 cup (47g) Calories 200, Fat Cal. 190,</text>
        <text class="nutrition" x="200" y="40">Total Fat 22g (34% DV), Sat Fat 3.5g (18% DV), Cholest. 5mg (2%</text>
        <text class="nutrition" x="200" y="50">DV), Sodium 200mg (8% DV), Total Carb. 3g (1% DV), Fiber 1g (4% DV),</text>
        <text class="nutrition" x="200" y="60">Sugars 1g, Protein 3g, Vitamin A (4% DV), Vitamin C (4% DV), Calcium</text>
        <text class="nutrition" x="200" y="70">(4% DV), Iron (4% DV).</text>
        <text class="nutrition" x="200" y="80">Percent Daily Values (DV) are based on a 2,000 calorie diet. Not a</text>
        <text class="nutrition" x="200" y="90">significant source of trans fat. Ingredients: Extra virgin olive oil, onion,</text>
        <text class="nutrition" x="200" y="100">basil, almonds, parmesan cheese (cow's milk, rennet, cheese</text>
        <text class="nutrition" x="200" y="110">cultures, salt), garlic, sea salt, paprika, cayenne pepper, and spices.</text>
        <text class="nutrition" x="200" y="122">Contains: nuts and cheese.</text>
      </g>

      <g transform="translate(200 512)">
        <path class="panel-fill" d="M152.4,63.1 A68,68 0 0 1 63.1,152.4 A68,68 0 0 1 -63.1,152.4 A68,68 0 0 1 -152.4,63.1 A68,68 0 0 1 -152.4,-63.1 A68,68 0 0 1 -63.1,-152.4 A68,68 0 0 1 63.1,-152.4 A68,68 0 0 1 152.4,-63.1 A68,68 0 0 1 152.4,63.1 Z"/>
        <path class="panel-rule" transform="scale(.92)" d="M152.4,63.1 A68,68 0 0 1 63.1,152.4 A68,68 0 0 1 -63.1,152.4 A68,68 0 0 1 -152.4,63.1 A68,68 0 0 1 -152.4,-63.1 A68,68 0 0 1 -63.1,-152.4 A68,68 0 0 1 63.1,-152.4 A68,68 0 0 1 152.4,-63.1 A68,68 0 0 1 152.4,63.1 Z"/>
        <ellipse class="flourish-area" role="img" aria-label="faded leaf flourishes behind the product name" cx="0" cy="-10" rx="120" ry="60"/>
      </g>
      <text class="brand-name" x="200" y="412">MARISOL GROVE</text>
      <circle class="logo-disc" cx="200" cy="440" r="21"/>
      <text class="logo-initials" x="200" y="446">MG</text>
      <text class="flavor-name" x="200" y="494">Cajun Pepper</text>
      <text class="product-word" x="200" y="545" font-size="54">Pesto</text>
      <text class="company-info" x="200" y="582">Orla Fine Foods, LLC.</text>
      <text class="company-info" x="200" y="596">218 Fennel Ave. Brookdale, NY</text>
      <text class="company-info" x="200" y="610">10457 +866-555-0192</text>
      <text class="company-info" x="200" y="624">www.marisolgrove.com</text>
      <text class="company-info" x="200" y="638">Ready to eat. Keep refrigerated, OK</text>
      <text class="company-info" x="200" y="652">to freeze</text>

      <path class="panel-fill" d="M43,880 H357 Q359,895 385,897 V1021 Q359,1023 357,1038 H43 Q41,1023 16,1021 V897 Q41,895 43,880 Z"/>
      <path class="panel-rule" d="M49,888 H351 Q354,901 377,904 V1014 Q354,1017 351,1030 H49 Q46,1017 24,1014 V904 Q46,901 49,888 Z"/>
      <text class="brand-name" x="200" y="912" font-size="13">MARISOL GROVE</text>
      <text class="flavor-name" x="200" y="936" font-size="24">Cajun Pepper</text>
      <text class="product-word" x="200" y="992" font-size="62">Pesto</text>
      <text class="tagline" x="200" y="1018">most delicious</text>
      <text class="net-weight" x="30" y="927">Net Wt.</text>
      <text class="net-weight" x="30" y="950">5.75 oz</text>
      <text class="net-weight" x="30" y="973">(162g)</text>
      <circle class="logo-disc" cx="352" cy="955" r="21"/>
      <text class="logo-initials" x="352" y="961">MG</text>
    </svg>
  </section>

</main>
</body>
</html>
```